The Marlow Method Diet Business Card

The Marlow Method is a revolutionary new diet approach. We need a fresh, different business card design for The Marlow Method. We would like the cards lettering and designed match with the color scheme of the logo(Orange,black,grey) and the website. We would like the front of the business card to be the pic of a scale(that people weigh themselves on).We have attached a pic we would like that kind of old school number scale. With the the words "want to lose weight?Eat what you crave! Change how it's made! Get moving! No gym required. Similar to our shirt design. At the Back of the card we would like our logo. My name Dwight Pemberly Jr. My telephone number 504-617-2254 my email dpemberlyjr@marlowmethod.example

Target Market(s)

Everyone who's looking to get into shape

Industry/Entity Type

Health And Wellness

Contact Information for Business Card

Name , company logo, weight scale. Want to have something people talk about that looks so refreshing

Colors
faa54b
f68d4d
000000
b2b2b2

Requirements
Must have
• Weight scale, logo and futuristic look. Nothing plain get creative baby!
Nice to have
• Something that would stand out in a crowd
Should not have
• Be boring or look like any other card or be anything like Brennick diet cards

```html
<!DOCTYPE html>
<html lang="en">
<head>
<meta charset="utf-8">
<title>The Marlow Method – Business Card</title>
<link rel="stylesheet" href="https://fonts.googleapis.com/css2?family=Open+Sans:wght@400;600;700&display=swap">
<style>
  :root {
    --orange-light: #faa54b;
    --orange: #f68d4d;
    --orange-deep: #f28a1e;
    --black: #000000;
    --grey: #b2b2b2;
    --steel: #8a8a8a;
    --charcoal: #1e1e1e;
    --ink: #2b2b2b;
    --white: #ffffff;
    --backdrop: #2c2e33;
  }
  * { box-sizing: border-box; margin: 0; padding: 0; }
  html, body {
    width: 1200px; height: 864px; overflow: hidden;
    background: var(--backdrop);
    font-family: "Open Sans", Arial, sans-serif;
  }
  .canvas { position: relative; width: 1200px; height: 864px; }

  .card {
    position: absolute;
    width: 580px; height: 330px;
    border-radius: 4px;
    overflow: hidden;
    box-shadow: 0 10px 30px rgba(0,0,0,.45);
  }

  /* Front */
  .card-front {
    left: 200px; top: 80px;
    background: linear-gradient(135deg, var(--orange-light) 0%, var(--orange-deep) 100%);
    color: var(--white);
  }
  .front-brand {
    position: absolute; left: 40px; top: 28px;
    width: 230px;
    font-weight: 600; font-size: 32px; line-height: 1.1;
    color: var(--white);
  }
  .pitch { position: absolute; left: 40px; top: 150px; }
  .pitch-question { font-weight: 700; font-size: 20px; margin-bottom: 6px; }
  .pitch-list { list-style: none; font-weight: 600; font-size: 15px; line-height: 1.75; }
  .pitch-list li::before { content: "\2022"; margin-right: 8px; }
  .scale-art {
    position: absolute; right: 36px; top: 60px;
    width: 240px; height: 220px; border-radius: 26px;
    background: linear-gradient(180deg, var(--grey) 0%, var(--steel) 22%, var(--charcoal) 48%, var(--charcoal) 100%);
  }

  /* Back */
  .card-back {
    left: 420px; top: 470px;
    background: var(--white);
    color: var(--ink);
  }
  .back-brand {
    position: absolute; left: 48px; top: 46px;
    display: flex; align-items: center; gap: 18px;
  }
  .brand-dot {
    flex: none;
    width: 70px; height: 70px; border-radius: 50%;
    background: var(--orange);
  }
  .brand-name {
    width: 280px;
    font-weight: 600; font-size: 38px; line-height: 1.08;
    color: var(--ink);
  }
  .name-rule {
    position: absolute; left: 0; right: 0; top: 186px;
    height: 2px; background: var(--orange-light);
  }
  .holder-name {
    position: absolute; right: 40px; top: 172px;
    background: var(--white); padding: 0 14px;
    font-weight: 700; font-size: 19px; color: var(--orange);
  }
  .contact {
    position: absolute; right: 40px; top: 236px;
    list-style: none; text-align: right;
    font-size: 15px; line-height: 1.7; color: var(--black);
  }
  .contact li { display: flex; align-items: center; justify-content: flex-end; gap: 8px; }
  .contact svg { width: 13px; height: 13px; fill: var(--orange); }
</style>
</head>
<body>
<main class="canvas">

  <section class="card card-front">
    <div class="front-brand">The Marlow Method</div>
    <div class="pitch">
      <p class="pitch-question">Want to lose weight?</p>
      <ul class="pitch-list">
        <li>Eat what you crave!</li>
        <li>Change how it's made!</li>
        <li>Get moving!</li>
        <li>No gym required</li>
      </ul>
    </div>
    <div class="scale-art" role="img" aria-label="Illustration of an old-school bathroom weight scale with a numbered dial"></div>
  </section>

  <section class="card card-back">
    <div class="back-brand">
      <span class="brand-dot"></span>
      <span class="brand-name">The Marlow Method</span>
    </div>
    <div class="name-rule"></div>
    <div class="holder-name">Dwight Pemberly Jr.</div>
    <ul class="contact">
      <li>504-617-2254
        <svg viewBox="0 0 24 24" aria-hidden="true"><path d="M6.6 10.8a15.1 15.1 0 0 0 6.6 6.6l2.2-2.2a1 1 0 0 1 1-.25 11.4 11.4 0 0 0 3.6.57 1 1 0 0 1 1 1V20a1 1 0 0 1-1 1A17 17 0 0 1 3 4a1 1 0 0 1 1-1h3.5a1 1 0 0 1 1 1c0 1.25.2 2.45.57 3.57a1 1 0 0 1-.25 1z"/></svg>
      </li>
      <li>dpemberlyjr@marlowmethod.example
        <svg viewBox="0 0 24 24" aria-hidden="true"><path d="M2 5h20v14H2z M2 5l10 8 10-8" fill="var(--orange)" stroke="#fff" stroke-width="1.5"/></svg>
      </li>
    </ul>
  </section>

</main>
</body>
</html>
```